Stationary Design For Youthful Disability Company

Hi Designers,
Looking to have our brand applied to a range of stationary items to professionalise our approach, we are a disability services company that aligns young carers with disabled youth and adults. Our stationary needs to look professional but can verge into a fun bright territory too.
Winning designer will be first contact for advertising campaign, form creation and web-design in January 2014.
Cheers,
Tom
Brightpath Disability Services
Design Briefs
Stationary.
Sleek fun and bright stationary that portrays a professional but youthful disability service. Company prides its self on delivering youthful carers to disabled clients.
Needed:
- Business Card - Letter Head - Email Signature
- Invoice / Quotation (blank branded paper) - Normal Envelope - A4 Envelope
- Stationary for future forms or documents. (Doesn't need to include all contacts, branding is enough).
Would be nice if we were able to edit numbers etc as we change them.
Include:
Lachlan Corrigan - Managing Director
M. 0478 295 604
E. lcorrigan@brightpathdisability.example
A. PO Box 87 Wexcombe 3391
ABN. 47392015863

```html
<!DOCTYPE html>
<html lang="en">
<head>
<meta charset="utf-8">
<title>Brightpath Disability Services – Stationery Suite</title>
<link rel="stylesheet" href="https://fonts.googleapis.com/css2?family=Open+Sans:wght@400;600;700&family=Exo+2:wght@700;800&family=Arimo:wght@400;700&display=swap">
<style>
  :root{
    --board:#dcdcdc;
    --paper:#f7f7f7;
    --paper-shade:#ebebeb;
    --ink-dark:#231f20;
    --ink-grey:#8a8a8a;
    --rule:#9a9a9a;
    --table-head:#b3b3b3;
    --card-grey:#d9d9d9;
    --white:#ffffff;
    --brand-blue:#1b8fd0;
    --toolbar:#eef2f7;
    --field-border:#b9c4d3;
    --spell:#d0021b;
  }
  *{box-sizing:border-box;margin:0;padding:0}
  html,body{width:1200px;height:1000px;overflow:hidden}
  body{background:var(--board);font-family:"Open Sans",Arial,sans-serif;position:relative}

  .sheet{position:absolute;box-shadow:0 2px 6px rgba(0,0,0,.35)}
  .sheet--paper{background:linear-gradient(180deg,var(--paper) 0%,var(--white) 55%,var(--paper-shade) 100%)}
  .sheet--dark{background:var(--ink-dark)}

  .brand{position:absolute;display:flex;align-items:center;gap:5px;font-family:"Exo 2",sans-serif;font-weight:800;letter-spacing:.02em;white-space:nowrap}
  .brand__dot{border-radius:50%;flex:none}
  .brand--stack{flex-direction:column;gap:6px;text-align:center;text-transform:uppercase;line-height:1}

  .sender{position:absolute;font-size:6.5px;line-height:9px;color:var(--ink-grey);font-weight:600}

  /* Letterhead */
  .letterhead{left:47px;top:141px;width:356px;height:504px}
  .letter__greeting{position:absolute;left:43px;top:131px;font-size:7px;font-weight:700;color:var(--ink-grey)}
  .letter__body{position:absolute;left:43px;top:155px;width:266px;font-size:5.8px;line-height:12.6px;font-weight:700;color:var(--ink-grey)}
  .letter__line{display:block;white-space:nowrap;text-align:justify;text-align-last:justify;height:12.6px}
  .letter__line--end{text-align-last:left}
  .letter__gap{display:block;height:12.6px}
  .letter__closing{position:absolute;left:43px;top:331px;font-size:6.6px;font-weight:700;color:var(--ink-grey)}
  .letter__signature{position:absolute;left:48px;top:352px;width:72px;height:34px;background:linear-gradient(90deg,#e6e6e6,#f2f2f2)}

  /* Invoice */
  .invoice{left:424px;top:141px;width:356px;height:504px}
  .field{position:absolute;font-size:7px;color:var(--ink-grey);font-weight:600;display:flex;align-items:flex-end;gap:3px}
  .field__line{display:inline-block;border-bottom:1px solid var(--rule);height:1px;margin-bottom:2px}
  .invoice__table{position:absolute;left:49px;top:122px;width:262px;height:291px;border:1px solid var(--rule)}
  .invoice__head{height:18px;background:var(--table-head);display:flex;justify-content:space-between;align-items:center;padding:0 21px 0 14px;font-size:8.5px;color:#3c3c3c;font-weight:600}
  .invoice__total{position:absolute;left:0;right:0;bottom:0;height:16px;border-top:1px solid var(--rule);font-size:8.5px;color:var(--ink-grey);padding-left:14px;line-height:15px}

  /* Envelopes */
  .envelope-a4{left:803px;top:141px;width:355px;height:504px}
  .envelope-a4__flap{position:absolute;left:803px;top:91px}
  .envelope-dl-back{left:47px;top:675px;width:356px;height:164px}
  .envelope-dl-back__flap{position:absolute;left:0;top:0}
  .envelope-dl-front{left:424px;top:675px;width:355px;height:164px}

  /* Business cards */
  .card-front{left:802px;top:671px;width:153px;height:85px}
  .card-back{left:1006px;top:671px;width:153px;height:85px;background:var(--card-grey)}
  .card__name{position:absolute;left:25px;top:25px;font-size:8.5px;color:#333}
  .card__details{position:absolute;left:71px;top:42px;font-size:5.6px;line-height:6.2px;color:#444;white-space:nowrap}

  /* Email signature */
  .email{left:802px;top:768px;width:357px;height:193px;background:var(--white);font-family:Arimo,Arial,sans-serif}
  .email__toolbar{height:15px;background:var(--toolbar);border-bottom:1px solid var(--field-border);display:flex;align-items:center;gap:4px;padding-left:4px;font-size:5.5px;color:#234}
  .tool{width:9px;height:8px;border-radius:1px;background:#b7c6da}
  .tool--select{width:36px;height:8px;background:var(--white);border:1px solid var(--field-border)}
  .email__help{margin-left:auto;margin-right:5px;width:7px;height:7px;border-radius:50%;background:var(--brand-blue)}
  .email__row{position:absolute;left:6px;display:flex;align-items:center;gap:4px;font-size:5.5px;color:#234}
  .email__input{position:absolute;left:34px;height:8px;width:314px;border:1px solid var(--field-border);background:var(--white);font-size:5.5px;line-height:7px;padding-left:2px}
  .email__suggest{position:absolute;left:44px;top:28px;width:112px;border:1px solid #999;background:#fffde0;font-size:4.4px;line-height:5.6px;padding:0 2px;color:#225;white-space:nowrap;overflow:hidden}
  .email__format{position:absolute;left:4px;top:57px;right:4px;height:10px;display:flex;gap:3px;align-items:center;border-bottom:1px solid var(--field-border)}
  .email__body{position:absolute;left:6px;top:74px;font-size:7px;color:#111;line-height:9px}
  .email__body p{margin-bottom:7px}
  .spell{text-decoration:underline wavy var(--spell)}
  .email__sig{position:absolute;left:6px;top:138px;font-size:6px;line-height:7.6px;color:#333}
  .email__sig small{display:block;font-size:5.6px;color:#777;font-family:"Open Sans",sans-serif}
</style>
</head>
<body>

<!-- Letterhead -->
<section class="sheet sheet--paper letterhead" aria-label="Letterhead">
  <div class="sender" style="left:43px;top:70px">Brightpath<br>PO Box 87<br>Wexcombe 3391</div>
  <div class="brand" style="right:44px;top:78px;font-size:10px;color:var(--ink-dark)">
    <span class="brand__dot" style="width:9px;height:9px;background:var(--brand-blue)"></span>Brightpath
  </div>
  <p class="letter__greeting">Dear Mrs Hale</p>
  <div class="letter__body">
    <span class="letter__line">Lorem ipsum dolor sit amet, consectetur adipisicing elit, sed do eiusmod tempor</span>
    <span class="letter__line">incididunt ut labore et dolore magna aliqua. Ut enim ad minim veniam, quis</span>
    <span class="letter__line">nostrud exercitation ullamco laboris nisi ut aliquip ex ea commodo consequat.</span>
    <span class="letter__line">Duis aute irure dolor in reprehenderit in voluptate velit esse cillum dolore eu</span>
    <span class="letter__line">fugiat nulla pariatur. Excepteur sint occaecat cupidatat non proident, sunt in</span>
    <span class="letter__line letter__line--end">culpa qui officia deserunt mollit anim id est laborum.</span>
    <span class="letter__line">Lorem ipsum dolor sit amet, consectetur adipisicing elit, sed do eiusmod tempor</span>
    <span class="letter__line">incididunt ut labore et dolore magna aliqua. Ut enim ad minim veniam, quis</span>
    <span class="letter__line">nostrud exercitation ullamco laboris nisi ut aliquip ex ea commodo consequat.</span>
    <span class="letter__gap"></span>
    <span class="letter__line">Lorem ipsum dolor sit amet, consectetur adipisicing elit, sed do eiusmod tempor</span>
    <span class="letter__line">incididunt ut labore et dolore magna aliqua. Ut enim ad minim veniam, quis</span>
    <span class="letter__line">nostrud exercitation ullamco laboris nisi ut aliquip ex ea commodo consequat.</span>
  </div>
  <p class="letter__closing">Sincerely,</p>
  <div class="letter__signature" role="img" aria-label="Handwritten signature"></div>
</section>

<!-- Invoice / quotation -->
<section class="sheet sheet--paper invoice" aria-label="Invoice form">
  <div class="sender" style="left:49px;top:43px">Brightpath<br>PO Box 87<br>Wexcombe 3391</div>
  <div class="brand" style="right:46px;top:42px;font-size:10px;color:var(--ink-dark)">
    <span class="brand__dot" style="width:9px;height:9px;background:var(--brand-blue)"></span>Brightpath
  </div>
  <div class="field" style="left:49px;top:96px">Supplier <span class="field__line" style="width:58px"></span></div>
  <div class="field" style="left:212px;top:98px">Supplier <span class="field__line" style="width:66px"></span></div>
  <div class="invoice__table">
    <div class="invoice__head"><span>Item</span><span>Amount</span></div>
    <div class="invoice__total">Total</div>
  </div>
  <div class="field" style="left:51px;top:433px;font-size:8px">Supplier <span class="field__line" style="width:82px"></span></div>
</section>

<!-- A4 envelope -->
<svg class="envelope-a4__flap" width="355" height="51" viewBox="0 0 355 51" aria-hidden="true">
  <defs><linearGradient id="flapA4" x1="0" y1="0" x2="0" y2="1"><stop offset="0" stop-color="#3a3536"/><stop offset="1" stop-color="#6b6566"/></linearGradient></defs>
  <polygon points="3,50 52,0 303,0 352,50" fill="url(#flapA4)"/>
</svg>
<section class="sheet sheet--dark envelope-a4" aria-label="A4 envelope">
  <div class="brand brand--stack" style="left:0;right:0;top:228px;font-size:30px;color:var(--white)">
    <span>Brightpath</span><span style="font-size:14px">Disability Services</span>
  </div>
</section>

<!-- DL envelope back -->
<section class="sheet sheet--paper envelope-dl-back" aria-label="Envelope back">
  <svg class="envelope-dl-back__flap" width="356" height="42" viewBox="0 0 356 42" aria-hidden="true">
    <polygon points="0,0 356,0 316,41 40,41" fill="var(--ink-dark)"/>
  </svg>
  <div class="brand" style="left:0;right:0;top:80px;justify-content:center;font-size:18px;color:var(--ink-dark)">
    <span class="brand__dot" style="width:14px;height:14px;background:var(--ink-dark)"></span>Brightpath
  </div>
</section>

<!-- DL envelope front -->
<section class="sheet sheet--dark envelope-dl-front" aria-label="Envelope front">
  <div class="brand brand--stack" style="left:0;right:0;top:82px;font-size:20px;color:var(--white);gap:4px">
    <span>Brightpath</span><span style="font-size:10px">Disability Services</span>
  </div>
</section>

<!-- Business card front -->
<section class="sheet sheet--dark card-front" aria-label="Business card front">
  <div class="brand brand--stack" style="left:0;right:0;top:35px;font-size:14px;color:var(--white);gap:3px">
    <span>Brightpath</span><span style="font-size:7px">Disability Services</span>
  </div>
</section>

<!-- Business card back -->
<section class="sheet card-back" aria-label="Business card back">
  <p class="card__name">Owen Harte</p>
  <div class="brand" style="left:26px;top:46px;font-size:5px;color:var(--ink-dark);gap:2px">
    <span class="brand__dot" style="width:5px;height:5px;background:var(--brand-blue)"></span>Brightpath
  </div>
  <div class="card__details">5518264<br>owen@harteworks.example<br>www.harteworks.example</div>
</section>

<!-- Email signature -->
<section class="sheet email" aria-label="Email signature">
  <div class="email__toolbar">
    <span class="tool"></span><span>Send</span><span class="tool"></span><span class="tool"></span><span class="tool"></span><span class="tool"></span><span class="tool"></span><span class="tool"></span><span class="tool"></span><span class="tool"></span><span class="tool"></span><span class="tool"></span><span>Options...</span><span class="tool--select tool"></span>
    <span class="email__help"></span>
  </div>
  <div class="email__row" style="top:19px"><span class="tool"></span>To...</div>
  <div class="email__input" style="top:19px">nad</div>
  <div class="email__row" style="top:33px"><span class="tool"></span>Cc...</div>
  <div class="email__input" style="top:32px"></div>
  <div class="email__suggest">nadia@harbourlane.example<br>Nadia Brooks [nadia.brooks@harbourlane.example]</div>
  <div class="email__row" style="top:45px">Subject:</div>
  <div class="email__input" style="top:44px">Next Week</div>
  <div class="email__format">
    <span class="tool tool--select" style="width:68px"></span><span class="tool tool--select" style="width:14px"></span>
    <span class="tool"></span><span class="tool"></span><span class="tool"></span><span class="tool"></span><span class="tool"></span><span class="tool"></span><span class="tool"></span><span class="tool"></span><span class="tool"></span><span class="tool"></span>
  </div>
  <div class="email__body">
    <p>Hi Nadia,</p>
    <p>Back to school already! Do you have time to go <span class="spell">throuh</span> the ICT plan today?</p>
    <p>Thanks,</p>
  </div>
  <div class="email__sig">
    Priya
    <small>PO Box 87<br>Wexcombe 3391</small>
    <div class="brand" style="position:static;margin-top:3px;font-size:11px;color:var(--brand-blue);gap:3px">
      <span class="brand__dot" style="width:8px;height:8px;background:var(--brand-blue)"></span>BRIGHTPATH
    </div>
  </div>
</section>

</body>
</html>
```